Corporate Two Sided Business Card

Looking for a Corporate "edgy" Modern look and feel for a business card

We are looking at two options. Dark background with our logo on it, white background with our logo on it - The background is more - Charcoal / Graphite then black

Details will be

Danielle Forsk

Licensee / Director

m. 0428 519 064

e. danielle@quorvela.com.au

quorvela.com.au

Target Market(s)

Professional Business people that refer use business and clients that own Investment Properties

Industry/Entity Type

Business

Contact Information for Business Card

Details will be

Danielle Forsk

Licensee / Director

m. 0428 519 064

quorvela.com.au

Font styles to use
Serif

Colors
000000
ec1f27
eeeeee
ffffff

Requirements
Must have
• Two options - White Background and Dark Background. - Two sided
Nice to have
• A design that is edgy, modern and new to look instead of boring style corporate cards - It should be a full integrated design
Should not have
• Block looking - Cheap.

```html
<!DOCTYPE html>
<html lang="en">
<head>
<meta charset="utf-8">
<title>Quorvela Business Card</title>
<link rel="stylesheet" href="https://fonts.googleapis.com/css2?family=Open+Sans:wght@400;600;700&family=Poppins:wght@600&display=swap">
<style>
  :root {
    --canvas: #e4e4e4;
    --charcoal: #474747;
    --charcoal-line: rgba(255,255,255,0.035);
    --paper: #f7f7f7;
    --paper-line: rgba(0,0,0,0.025);
    --ink: #4a4a4a;
    --ink-soft: #7a7a7a;
    --red: #ec1f27;
    --white: #ffffff;
  }
  * { margin: 0; padding: 0; box-sizing: border-box; }
  html, body { width: 1200px; height: 660px; overflow: hidden; }
  body {
    background: var(--canvas);
    font-family: "Open Sans", Arial, sans-serif;
    position: relative;
  }
  .card {
    position: absolute;
    top: 175px;
    width: 540px;
    height: 309px;
    box-shadow: 0 10px 30px rgba(0,0,0,0.18);
    overflow: hidden;
  }
  .card--front {
    left: 40px;
    background:
      repeating-linear-gradient(135deg, var(--charcoal-line) 0 2px, transparent 2px 6px),
      var(--charcoal);
  }
  .card--back {
    left: 620px;
    background:
      repeating-linear-gradient(135deg, var(--paper-line) 0 2px, transparent 2px 6px),
      var(--paper);
  }
  .brand {
    position: absolute;
    display: flex;
    align-items: center;
    font-family: "Poppins", "Open Sans", sans-serif;
    font-weight: 600;
    letter-spacing: -0.5px;
  }
  .brand__mark {
    background: var(--red);
    flex: none;
  }
  .card--front .brand {
    left: 50%;
    top: 50%;
    transform: translate(-50%, -50%);
    font-size: 62px;
    color: var(--white);
    gap: 14px;
  }
  .card--front .brand__mark { width: 34px; height: 34px; }
  .card--back .brand {
    left: 38px;
    top: 140px;
    font-size: 36px;
    color: var(--ink);
    gap: 9px;
  }
  .card--back .brand__mark { width: 20px; height: 20px; }
  .holder {
    position: absolute;
    right: 44px;
    top: 28px;
    text-align: right;
  }
  .holder__name {
    font-size: 19px;
    color: var(--ink-soft);
    line-height: 1.2;
  }
  .holder__name strong { color: var(--ink); font-weight: 700; }
  .holder__role {
    font-size: 12px;
    font-weight: 600;
    color: var(--red);
    letter-spacing: 0.3px;
  }
  .holder-bar {
    position: absolute;
    right: 30px;
    top: 26px;
    width: 3px;
    height: 30px;
    background: var(--red);
  }
  .rule {
    position: absolute;
    left: 0;
    height: 2px;
    background: var(--red);
  }
  .rule--top { top: 92px; width: 520px; }
  .rule--bottom { top: 208px; width: 300px; }
  .contact {
    position: absolute;
    left: 38px;
    top: 222px;
    list-style: none;
  }
  .contact__item {
    display: flex;
    align-items: center;
    gap: 12px;
    font-size: 13px;
    font-weight: 600;
    color: var(--ink);
    height: 24px;
  }
  .contact__icon { width: 12px; height: 12px; flex: none; }
</style>
</head>
<body>
  <section class="card card--front" aria-label="Card front">
    <div class="brand"><span class="brand__mark"></span>quorvela</div>
  </section>

  <section class="card card--back" aria-label="Card back">
    <div class="holder">
      <p class="holder__name"><strong>Danielle</strong> Forsk</p>
      <p class="holder__role">Licensee / Director</p>
    </div>
    <span class="holder-bar"></span>
    <span class="rule rule--top"></span>

    <div class="brand"><span class="brand__mark"></span>quorvela</div>

    <span class="rule rule--bottom"></span>
    <ul class="contact">
      <li class="contact__item">
        <svg class="contact__icon" viewBox="0 0 12 12" aria-hidden="true">
          <rect x="2.5" y="0.5" width="7" height="11" rx="1.2" fill="none" stroke="#ec1f27" stroke-width="1.4"/>
          <circle cx="6" cy="9.3" r="0.8" fill="#ec1f27"/>
        </svg>
        0428 519 064
      </li>
      <li class="contact__item">
        <svg class="contact__icon" viewBox="0 0 12 12" aria-hidden="true">
          <rect x="0.5" y="2" width="11" height="8" fill="#ec1f27"/>
          <path d="M0.5 2 L6 6.5 L11.5 2" fill="none" stroke="#ffffff" stroke-width="1.1"/>
        </svg>
        e. danielle@quorvela.com.au
      </li>
      <li class="contact__item">
        <svg class="contact__icon" viewBox="0 0 12 12" aria-hidden="true">
          <circle cx="6" cy="6" r="5.5" fill="#ec1f27"/>
          <ellipse cx="6" cy="6" rx="2.3" ry="5.5" fill="none" stroke="#ffffff" stroke-width="0.9"/>
          <line x1="0.5" y1="6" x2="11.5" y2="6" stroke="#ffffff" stroke-width="0.9"/>
        </svg>
        www.quorvela.com.au
      </li>
    </ul>
  </section>
</body>
</html>
```